Website Design for Architecture Practice

I need a home page and one sidebar/content page for an Architecture practice delivered in PSD.

This archictecture practice specialises in one-off, high end homes and commercial properties (restaurant) heavily influenced by Dorian Vessey Kent, particularly his work on the Tarrowby Museum

I am looking for a home page, and a generic content page where we can outline our services, and showcase our homes.

http://notes.qorvenuni.edu.au/studio/Tarrowby%20Lisdane%202.jpg

Target Market(s)

30-70yr old (typically wealthy) property buyers, developers and investors

Industry/Entity Type

Architecture

Number of Pages Required

2 page

Font styles to use
Serif
Sans Serif

Requirements
Must have
• Home page design
• a Content Page design (ie, top nav with sidebar)
Nice to have
• Use any Dorian Vessey Kent images you can find via google etc as placeholders for our own photography (ie they don't need to be licensed as we will be replacing with our own commissioned photography). Full color preferred but feel free to experiment with treating any images as you see fit.

```html
<!DOCTYPE html>
<html lang="en">
<head>
<meta charset="utf-8">
<title>Calder Nine – Architectural Services</title>
<link rel="stylesheet" href="https://fonts.googleapis.com/css2?family=Raleway:wght@400;500;600;700&family=Open+Sans:wght@400;600&display=swap">
<style>
  :root {
    --ink-dark: #1f2326;
    --ink-mid: #2b3034;
    --teal: #2fc6b8;
    --teal-light: #5fdccf;
    --teal-deep: #1fa99c;
    --page-bg: #ececec;
    --white: #ffffff;
    --text: #444a4f;
    --muted: #8b9196;
    --rule: #dcdcdc;
  }
  * { box-sizing: border-box; margin: 0; padding: 0; }
  html, body { width: 828px; height: 1200px; overflow: hidden; }
  body {
    background: var(--page-bg);
    font-family: "Open Sans", Arial, sans-serif;
    color: var(--text);
    position: relative;
  }
  .site-header {
    height: 55px;
    background: var(--ink-dark);
    position: relative;
  }
  .site-header .inner {
    position: absolute; left: 124px; width: 580px; top: 0; height: 55px;
    display: flex; align-items: center; justify-content: space-between;
  }
  .brand {
    font-family: "Raleway", Arial, sans-serif;
    color: var(--white); font-size: 23px; font-weight: 500; letter-spacing: .3px;
  }
  .call {
    text-align: right; font-family: "Raleway", Arial, sans-serif;
  }
  .call small { display: block; color: var(--teal); font-size: 10px; }
  .call span { display: flex; align-items: center; gap: 5px; color: var(--white); font-size: 13px; font-weight: 600; }

  .wrap { position: absolute; left: 124px; width: 580px; }

  .main-nav {
    top: 55px; height: 22px; background: var(--teal);
    display: flex; justify-content: center; gap: 44px; align-items: center;
  }
  .main-nav a {
    font-family: "Raleway", Arial, sans-serif; font-size: 9px; font-weight: 700;
    color: var(--white); text-decoration: none; letter-spacing: .4px;
  }

  .hero {
    top: 77px; height: 331px;
    background: linear-gradient(180deg, #c9d0d3 0%, #e4e7e6 35%, #b8bfbf 70%, #6e7a78 100%);
  }
  .hero-caption {
    position: absolute; left: 38px; top: 128px; width: 360px; padding: 12px 16px;
    background: rgba(30, 34, 38, .55);
  }
  .hero-caption h1 {
    font-family: "Raleway", Arial, sans-serif; font-weight: 400; font-size: 28px; color: var(--white);
  }
  .hero-caption .lead { color: var(--teal-light); font-size: 13px; margin: 2px 0 8px; font-family: "Raleway", Arial, sans-serif; }
  .hero-caption p.body { color: #e3e6e8; font-size: 8px; line-height: 1.5; }
  .slider-dots {
    position: absolute; left: 150px; top: 270px; display: flex; gap: 6px;
  }
  .slider-dots i { width: 8px; height: 8px; border-radius: 50%; background: rgba(255,255,255,.55); }
  .slider-dots i.active { background: var(--white); }

  .feature-band {
    top: 408px; height: 130px;
    background: linear-gradient(180deg, var(--teal-light) 0%, var(--teal) 100%);
    display: flex; justify-content: space-around; align-items: center; padding: 0 14px;
  }
  .feature {
    display: flex; align-items: center; gap: 10px; width: 170px; color: var(--white);
  }
  .feature h3 { font-family: "Raleway", Arial, sans-serif; font-size: 13px; font-weight: 500; }
  .feature p { font-size: 7px; line-height: 1.5; opacity: .9; margin-top: 2px; }

  .content {
    top: 538px; height: 580px; background: var(--white);
  }
  .services {
    position: absolute; left: 24px; right: 24px; top: 26px;
    display: grid; grid-template-columns: repeat(3, 1fr); gap: 16px;
  }
  .service .photo { height: 96px; background: linear-gradient(135deg, #9fb1bd, #d8dee2 60%, #7d8f98); }
  .service .photo.b { background: linear-gradient(135deg, #b9c6cf, #eef1f3 55%, #8fa4b0); }
  .service .photo.c { background: linear-gradient(135deg, #7e98ad, #c9d4dc 55%, #a49582); }
  .service h4 {
    font-family: "Raleway", Arial, sans-serif; font-size: 12px; font-weight: 600; color: var(--ink-mid);
    text-align: center; margin: 10px 0 5px; letter-spacing: .3px;
  }
  .service p { font-size: 7px; line-height: 1.55; color: var(--muted); text-align: center; }

  .section-title {
    position: absolute; left: 0; right: 0; text-align: center;
    font-family: "Raleway", Arial, sans-serif; font-size: 15px; font-weight: 600; color: var(--ink-mid); letter-spacing: .5px;
  }
  .projects {
    position: absolute; left: 24px; right: 24px; top: 282px;
    display: grid; grid-template-columns: repeat(4, 1fr); gap: 10px;
  }
  .project { background: var(--white); box-shadow: 0 2px 6px rgba(0,0,0,.12); padding-bottom: 10px; }
  .project .photo { height: 82px; background: linear-gradient(160deg, #5e8fc2, #b5cde0 55%, #d9d9d4); }
  .project:nth-child(2) .photo { background: linear-gradient(160deg, #7fa8cf, #e6ecef 55%, #b8a989); }
  .project:nth-child(3) .photo { background: linear-gradient(160deg, #4d87c4, #cfdde8 50%, #c7b28d); }
  .project:nth-child(4) .photo { background: linear-gradient(160deg, #8ab4da, #e7ebee 55%, #9c9f9e); }
  .project h5 {
    font-family: "Raleway", Arial, sans-serif; color: var(--teal-deep); font-size: 10px; font-weight: 600;
    text-align: center; margin: 8px 0 4px;
  }
  .project p { font-size: 6.5px; line-height: 1.5; color: var(--muted); text-align: center; padding: 0 8px; }

  .clients {
    position: absolute; left: 24px; right: 24px; top: 530px;
    display: flex; justify-content: space-between; align-items: center;
  }
  .client {
    font-family: "Raleway", Arial, sans-serif; font-weight: 700; font-size: 14px; color: #9da2a6;
  }

  .site-footer {
    position: absolute; left: 0; right: 0; top: 1118px; height: 82px; background: var(--ink-dark);
  }
  .site-footer .inner {
    position: absolute; left: 124px; width: 580px; top: 0; height: 82px;
    display: flex; justify-content: space-between; align-items: center;
  }
  .footer-links { display: flex; gap: 6px; font-family: "Raleway", Arial, sans-serif; font-size: 8px; font-weight: 700; color: var(--white); }
  .footer-links span { color: var(--muted); }
  .copyright { font-size: 7px; color: var(--muted); margin-top: 6px; }
  .social { display: flex; gap: 5px; }
  .social i { width: 18px; height: 18px; border-radius: 50%; background: var(--teal); }
</style>
</head>
<body>

<header class="site-header">
  <div class="inner">
    <div class="brand">Calder Nine</div>
    <div class="call">
      <small>Call us Now</small>
      <span>
        <svg width="11" height="11" viewBox="0 0 24 24" aria-hidden="true"><path fill="#fff" d="M6.6 10.8a15.1 15.1 0 0 0 6.6 6.6l2.2-2.2c.3-.3.7-.4 1-.2 1.1.4 2.3.6 3.6.6.6 0 1 .4 1 1V20c0 .6-.4 1-1 1A17 17 0 0 1 3 4c0-.6.4-1 1-1h3.5c.6 0 1 .4 1 1 0 1.3.2 2.5.6 3.6.1.3 0 .7-.2 1z"/></svg>
        555.204.7781
      </span>
    </div>
  </div>
</header>

<nav class="wrap main-nav">
  <a href="#">HOME</a><a href="#">ABOUT US</a><a href="#">PROJECTS</a><a href="#">SERVICES</a><a href="#">NEWS</a><a href="#">CONTACT</a>
</nav>

<section class="wrap hero" role="img" aria-label="Photograph of a curving white spiral museum building on a city street">
  <div class="hero-caption">
    <h1>Architectural Services</h1>
    <p class="lead">Praesent sit amet elit dolor ac dictum</p>
    <p class="body">Quisque vel lacus sed nibh tempus faucibus vitae at magna. Donec sit amet ligula nec risus aliquet blandit non eget urna.</p>
  </div>
  <div class="slider-dots"><i class="active"></i><i></i><i></i><i></i></div>
</section>

<section class="wrap feature-band">
  <div class="feature">
    <svg width="38" height="34" viewBox="0 0 38 34" fill="none" stroke="#fff" stroke-width="1.4" aria-hidden="true">
      <rect x="4" y="6" width="14" height="26"/><rect x="18" y="14" width="16" height="18"/>
      <path d="M8 11h2M13 11h2M8 16h2M13 16h2M8 21h2M13 21h2M22 19h2M28 19h2M22 24h2M28 24h2M1 32h36"/>
    </svg>
    <div><h3>Commercial Building</h3><p>Aliquam erat volutpat nunc sed tortor vitae lorem blandit mattis.</p></div>
  </div>
  <div class="feature">
    <svg width="38" height="34" viewBox="0 0 38 34" fill="none" stroke="#fff" stroke-width="1.4" aria-hidden="true">
      <rect x="3" y="10" width="32" height="22"/><path d="M1 10l4-7h28l4 7M15 32V20h8v12M7 16h5M26 16h5"/>
    </svg>
    <div><h3>Restaurants</h3><p>Aliquam erat volutpat nunc sed tortor vitae lorem blandit mattis.</p></div>
  </div>
  <div class="feature">
    <svg width="38" height="34" viewBox="0 0 38 34" fill="none" stroke="#fff" stroke-width="1.4" aria-hidden="true">
      <path d="M3 16L19 3l16 13M7 13v19h24V13M15 32v-9h8v9"/><rect x="10" y="17" width="4" height="4"/><rect x="24" y="17" width="4" height="4"/>
    </svg>
    <div><h3>High end Homes</h3><p>Aliquam erat volutpat nunc sed tortor vitae lorem blandit mattis.</p></div>
  </div>
</section>

<main class="wrap content">
  <div class="services">
    <article class="service">
      <div class="photo" role="img" aria-label="Architects reviewing plans at a desk"></div>
      <h4>WHAT WE DO</h4>
      <p>Sed ut perspiciatis unde omnis iste natus error sit voluptatem accusantium doloremque laudantium totam rem aperiam eaque ipsa quae ab illo.</p>
    </article>
    <article class="service">
      <div class="photo b" role="img" aria-label="Team working together in a bright studio"></div>
      <h4>HOW WE WORK</h4>
      <p>Sed ut perspiciatis unde omnis iste natus error sit voluptatem accusantium doloremque laudantium totam rem aperiam eaque ipsa quae ab illo.</p>
    </article>
    <article class="service">
      <div class="photo c" role="img" aria-label="Sculptural metal-clad museum beside a river"></div>
      <h4>SERVICES PROVIDE</h4>
      <p>Sed ut perspiciatis unde omnis iste natus error sit voluptatem accusantium doloremque laudantium totam rem aperiam eaque ipsa quae ab illo.</p>
    </article>
  </div>

  <h2 class="section-title" style="top:252px">LATEST PROJECTS</h2>
  <div class="projects">
    <article class="project"><div class="photo" role="img" aria-label="Modern curved building against a blue sky"></div><h5>Project Title</h5><p>Lorem ipsum dolor sit amet consectetur elit sed do.</p></article>
    <article class="project"><div class="photo" role="img" aria-label="White spiral gallery exterior"></div><h5>Project Title</h5><p>Lorem ipsum dolor sit amet consectetur elit sed do.</p></article>
    <article class="project"><div class="photo" role="img" aria-label="Stone and glass villa with terraces"></div><h5>Project Title</h5><p>Lorem ipsum dolor sit amet consectetur elit sed do.</p></article>
    <article class="project"><div class="photo" role="img" aria-label="Contemporary museum facade"></div><h5>Project Title</h5><p>Lorem ipsum dolor sit amet consectetur elit sed do.</p></article>
  </div>

  <h2 class="section-title" style="top:496px;font-weight:500;color:var(--muted);font-size:13px">OUR CLIENTS</h2>
  <div class="clients">
    <span class="client">Norvane</span>
    <span class="client">Quellis</span>
    <span class="client">Tressa</span>
    <span class="client">Ambrin</span>
    <span class="client">Calvoro</span>
    <span class="client">Pentrell</span>
  </div>
</main>

<footer class="site-footer">
  <div class="inner">
    <div>
      <div class="footer-links">HOME <span>|</span> ABOUT US <span>|</span> SERVICES <span>|</span> OUR PROJECTS <span>|</span> CONTACT US</div>
      <p class="copyright">© 2015 Calder Nine. All rights reserved.</p>
    </div>
    <div class="social"><i></i><i></i><i></i><i></i></div>
  </div>
</footer>

</body>
</html>
```